New Zealand Export company needs business cards

We need new business cards to match our new logo for a company based in New Zealand who deal specifically with the Pacific Islands. We source, consolidate and ship products out of New Zealand to the Pacific Islands. Will attach our old ones and also new logo.
Would like the Islands we deal with and the areas of work we have access to, to be included on the business cards.

Contact Information for Business Card

T +64 9 571 3048
F +64 9 571 6285
12-18 Kowhai Lane, Drury, 2113
PO Box 814, Drury, Auckland 2247, New Zealand
www.falconfreight.example.nz
E sales@falconfreight.example.nz

Font styles to use
Sans Serif

Colors
85abd2
33a6d7
ffffff

Requirements
Must have
• A company of PWM

```html
<!DOCTYPE html>
<html lang="en">
<head>
<meta charset="utf-8">
<title>Falcon Freight business cards</title>
<link href="https://fonts.googleapis.com/css2?family=Roboto:wght@400;500;700&display=swap" rel="stylesheet">
<style>
  :root {
    --navy: #0d5aa7;
    --sky: #33a6d7;
    --soft: #85abd2;
    --white: #ffffff;
    --ink: #3a3f44;
    --stage: #9c9c9c;
    --leaf: #6fa640;
    --leaf-light: #9cc46a;
  }
  * { margin: 0; padding: 0; box-sizing: border-box; }
  html, body { width: 1172px; height: 1200px; overflow: hidden; }
  body {
    background: var(--stage);
    font-family: 'Roboto', Arial, sans-serif;
    position: relative;
  }
  .card {
    position: absolute;
    left: 214px;
    width: 744px;
    border-radius: 26px;
    overflow: hidden;
  }
  .card-front {
    top: 122px; height: 425px;
    background: linear-gradient(180deg, #b8e4f5 0%, #d9f1fa 45%, #8fd2dc 60%, #6fc2cf 100%);
  }
  .card-back {
    top: 645px; height: 430px;
    background: linear-gradient(180deg, #d6e2f2 0%, #e7eef8 40%, #d3e9ef 46%, #e8f0f3 58%, #eeeff0 100%);
  }
  .brand {
    position: absolute;
    left: 0; right: 0;
    display: flex; align-items: center; justify-content: center; gap: 16px;
  }
  .brand-mark { width: 46px; height: 46px; background: var(--sky); }
  .brand-name {
    font-weight: 700; font-size: 44px; letter-spacing: 2px;
    color: var(--navy);
  }
  .card-front .brand { top: 44px; }
  .island-photo {
    position: absolute; left: 130px; top: 134px; width: 470px; height: 122px;
    border-radius: 6px;
    background: linear-gradient(180deg, var(--leaf-light) 0%, var(--leaf) 100%);
  }
  .heading {
    position: absolute; top: 165px;
    font-weight: 700; font-size: 20px; color: var(--navy);
  }
  .heading-islands { left: 27px; }
  .heading-industries { right: 26px; }
  .list {
    position: absolute; top: 263px;
    font-size: 18.5px; line-height: 25px; color: #1d3a55;
  }
  .list-islands { left: 27px; }
  .list-industries { right: 26px; text-align: right; }
  .dot { color: var(--navy); font-size: 15px; padding: 0 3px; }
  .tagline {
    position: absolute; left: 0; right: 0; bottom: 0; height: 50px;
    background: var(--navy); color: var(--white);
    font-weight: 700; font-size: 29.5px; text-align: center; line-height: 50px;
  }
  .card-back .brand { top: 78px; }
  .person-name {
    position: absolute; top: 195px; left: 0; right: 0; text-align: center;
    font-weight: 700; font-size: 28px; color: var(--navy);
  }
  .person-role {
    position: absolute; top: 231px; left: 0; right: 0; text-align: center;
    font-size: 20px; color: var(--ink);
  }
  .address {
    position: absolute; top: 285px; right: 400px; text-align: right;
    font-size: 18.5px; line-height: 24.5px; color: var(--ink);
  }
  .contact-divider {
    position: absolute; top: 290px; left: 372px; width: 2px; height: 64px; background: var(--sky);
  }
  .contacts {
    position: absolute; top: 285px; left: 398px;
    font-size: 19px; line-height: 24.5px; color: var(--ink); list-style: none;
  }
  .contacts li { display: flex; align-items: center; gap: 9px; }
  .contacts svg { width: 16px; height: 16px; }
  .web-band { position: absolute; left: 0; right: 0; bottom: 0; height: 38px; }
  .web-band svg { position: absolute; inset: 0; }
  .web-address {
    position: absolute; left: 0; right: 0; bottom: 5px; text-align: center;
    font-size: 18px; color: var(--white);
  }
</style>
</head>
<body>

<section class="card card-front">
  <div class="island-photo" role="img" aria-label="Photograph of a small forested tropical island in calm turquoise sea"></div>
  <div class="brand">
    <span class="brand-mark"></span>
    <span class="brand-name">FALCON FREIGHT</span>
  </div>
  <h2 class="heading heading-islands">ISLANDS</h2>
  <h2 class="heading heading-industries">INDUSTRIES</h2>
  <p class="list list-islands">
    <span class="dot">●</span>Cook Islands<span class="dot">●</span>Papua New Guinea<span class="dot">●</span>Tahiti<br>
    <span class="dot">●</span>Tuvalu&nbsp; Tokelau<span class="dot">●</span>Fiji&nbsp;&nbsp; Kiribati<span class="dot">●</span>Samoa<br>
    <span class="dot">●</span>New Caledonia<span class="dot">●</span>Tonga<span class="dot">●</span>Norfolk Island<br>
    <span class="dot">●</span>Solomon Islands<span class="dot">●</span>Vanuatu
  </p>
  <p class="list list-industries">
    Hardware<span class="dot">●</span>Automotive<span class="dot">●</span><br>
    Homewares<span class="dot">●</span>Aid Solutions<span class="dot">●</span><br>
    Hospitality<span class="dot">●</span>Safety Equipment<span class="dot">●</span><br>
    Environmental Resources<span class="dot">●</span>
  </p>
  <div class="tagline">SUPPLYING THE PACIFIC FOR OVER 38 YEARS</div>
</section>

<section class="card card-back" role="img" aria-label="Calm beach and sea backdrop">
  <div class="brand">
    <span class="brand-mark"></span>
    <span class="brand-name">FALCON FREIGHT</span>
  </div>
  <h1 class="person-name">TESSA ROWAN</h1>
  <p class="person-role">Sales Manager</p>
  <p class="address">
    12-18 Kowhai Lane, Drury, 2113<br>
    PO Box 814, Drury Auckland 2247<br>
    New Zealand
  </p>
  <div class="contact-divider"></div>
  <ul class="contacts">
    <li>
      <svg viewBox="0 0 16 16"><path d="M3 1.5l3 3-1.6 1.8c.9 2 2.3 3.4 4.3 4.3L10.5 9l3 3-1.8 2.2C6.5 14 2 9.5 1 3.6z" fill="none" stroke="#0d5aa7" stroke-width="1.5"/></svg>
      +64 9 571 3048
    </li>
    <li>
      <svg viewBox="0 0 16 16"><rect x="4" y="1" width="8" height="14" rx="1.5" fill="none" stroke="#0d5aa7" stroke-width="1.5"/><circle cx="8" cy="12.5" r="0.9" fill="#0d5aa7"/></svg>
      +64 9 571 6285
    </li>
    <li>
      <svg viewBox="0 0 16 16"><rect x="1" y="3.5" width="14" height="9" fill="#0d5aa7"/><path d="M1 3.5l7 5 7-5" fill="none" stroke="#ffffff" stroke-width="1.2"/></svg>
      sales@falconfreight.example.nz
    </li>
  </ul>
  <div class="web-band">
    <svg viewBox="0 0 744 38" preserveAspectRatio="none"><path d="M0 20H246L258 0H486L498 20H744V38H0Z" fill="#0d5aa7"/></svg>
    <span class="web-address">www.falconfreight.example.nz</span>
  </div>
</section>

</body>
</html>
```